Walt’s Brick Oven Pizza Menu & Logo design

Looking for something that I can put on an 8.5x14 and also larger for an in-house menu to laminate. This is for a pizzeria, it doesn’t need to have that logo on it, I need a new design that is clean and I can use for shirts and signs. Want something modern and clean. This pizzeria is established and we are looking to rebrand. I have the current logo on the menu submission.

Target Market(s)

Looking for a new logo and menu design for my Pizzeria.

Industry/Entity Type

restaurant

Font styles to use
Sans Serif

Requirements
Must have
• Clean and fresh design for the logo that works for the menu, shirts, and signs.
Nice to have
• Open to any design, I want something completely catchy and updated.

```html
<!DOCTYPE html>
<html lang="en">
<head>
<meta charset="utf-8">
<title>Walt’s Brick Oven Pizza – Menu</title>
<link href="https://fonts.googleapis.com/css2?family=Bebas+Neue&family=Montserrat:wght@400;700&display=swap" rel="stylesheet">
<style>
:root{
  --stage:#3c414d;
  --paper:#f3f3f1;
  --red:#c4161c;
  --red-dark:#8f1014;
  --gold:#c29317;
  --gold-light:#ddab2a;
  --ink:#111;
  --muted:#555;
  --black:#1b1b1b;
  --rule:#6b6b6b;
}
*{margin:0;padding:0;box-sizing:border-box}
html,body{width:1200px;height:805px;overflow:hidden;background:var(--stage)}
body{position:relative;font-family:"Montserrat",sans-serif;color:var(--ink)}
.menu{position:absolute;left:36px;top:60px;width:1128px;height:684px;background:var(--paper);overflow:hidden}
.band{position:absolute;top:0;height:82px;background:linear-gradient(180deg,var(--red-dark),var(--red) 45%,#a81318);}
.band--left{left:0;width:429px}
.band--right{right:0;width:429px}
.section{position:absolute;background:var(--paper);border:1px solid var(--rule);border-top:none}
.section__title{background:var(--gold);color:#fff;font-family:"Bebas Neue",sans-serif;font-size:17px;line-height:21px;height:21px;padding-left:8px;letter-spacing:.2px;margin:0 -1px}
.items{padding:4px 7px 3px 8px}
.item__row{display:flex;justify-content:space-between;font-weight:700;font-size:9.2px;line-height:13px}
.item__desc{font-size:8.6px;line-height:13px;color:var(--muted)}
.toppings{position:absolute;left:24px;top:492px;width:362px;height:143px;background:var(--gold-light);padding:6px 8px;font-size:8.6px;line-height:13px;color:#fff}
.toppings strong{color:#fff}
.toppings .opts{color:#2a1f00}
.hero{position:absolute;left:429px;top:0;width:270px;height:438px;background:var(--black)}
.hero svg{position:absolute;left:0;bottom:-14px}
.brand{position:absolute;top:70px;left:0;width:100%;text-align:center;font-family:"Bebas Neue",sans-serif;color:#fff;line-height:.9}
.brand__top{font-size:70px}
.brand__bottom{font-size:40px}
.brand__rule{position:absolute;left:88px;top:202px;width:134px;height:4px;background:var(--red)}
.tagline{position:absolute;left:0;width:100%;text-align:center;font-family:"Bebas Neue",sans-serif;color:#fff;font-size:21px;line-height:27px}
.tagline--a{top:229px}
.star{position:absolute;left:120px;top:288px}
.fav{position:absolute;left:0;width:100%;text-align:center;font-family:"Bebas Neue",sans-serif;color:#fff}
.fav__label{top:325px;font-size:22px;line-height:24px}
.fav__rule{position:absolute;left:30px;top:351px;width:211px;height:1px;background:#aaa}
.fav__name{top:360px;font-size:22px;line-height:27px}
.sizes{font-weight:700;white-space:nowrap}
.sizes span{font-weight:400;color:var(--muted);margin:0 2px}
.sizes i{font-style:normal;border-left:1px solid #999;margin-left:3px}
.salad .item__desc{width:232px}
.dressings{position:absolute;left:749px;top:500px;font-size:8.6px;line-height:13px;color:var(--muted)}
.dressings strong{color:var(--ink)}
.photo{position:absolute;left:742px;top:544px;width:386px;height:140px;background:linear-gradient(90deg,#6b4a35 0%,#8a5c3e 25%,#d9842e 45%,#c8462a 70%,#b9572c 100%)}
</style>
</head>
<body>
<main class="menu">
  <div class="band band--left"></div>
  <div class="band band--right"></div>

  <section class="section" style="left:24px;top:50px;width:362px;height:132px">
    <h2 class="section__title">Lunch Specials</h2>
    <div class="items">
      <div class="item__row"><span>2 Slices of Pizza &amp; 20 oz Drink</span><span>$8.99</span></div>
      <div class="item__desc">Choose your drink. Add a slice topping if you'd like.</div>
      <div class="item__row"><span>Slice of Pizza &amp; Small Salad &amp; 20 oz Drink</span><span>$9.99</span></div>
      <div class="item__desc">Choice of dressing and drink.</div>
      <div class="item__row"><span>Slice of Pizza &amp; 6 Wings &amp; 20 oz Drink</span><span>$12.99</span></div>
      <div class="item__desc">Choose wing sauce and your drink.</div>
      <div class="item__row"><span>Any Philly Cheesesteak &amp; 20 oz Drink</span><span>$10.99</span></div>
      <div class="item__desc">Choose your drink. Philly add-ons available.</div>
    </div>
  </section>

  <section class="section" style="left:24px;top:192px;width:362px;height:132px">
    <h2 class="section__title">Daily Specials</h2>
    <div class="items">
      <div class="item__row"><span>Medium Cheese Pizza &amp; 10 Wings</span><span>$29.95</span></div>
      <div class="item__desc">Choose wing style and sauce.</div>
      <div class="item__row"><span>Large 16" Cheese Pizza &amp; 20 Wings</span><span>$39.95</span></div>
      <div class="item__desc">Choose wing style and sauce, then add pizza toppings if you'd like.</div>
      <div class="item__row"><span>Large 16" Pizzas</span><span>$30.99</span></div>
      <div class="item__desc">Add toppings to either pie.</div>
      <div class="item__row"><span>18" Cheese Pizza, 24 Wings &amp; 2 Liter Soda</span><span>$45.99</span></div>
      <div class="item__desc">Choose wing style, sauce, soda, and pizza toppings.</div>
    </div>
  </section>

  <section class="section" style="left:24px;top:334px;width:362px;height:158px">
    <h2 class="section__title">Calzones</h2>
    <div class="items">
      <div class="item__row"><span>Traditional Calzone</span><span>$11.99</span></div>
      <div class="item__desc">Mozzarella &amp; Ricotta Cheese.</div>
      <div class="item__row"><span>NY Supreme Calzone</span><span>$14.99</span></div>
      <div class="item__desc">Pepperoni, Sausage, Mushrooms, Onions, Green Peppers,<br>Mozzarella, &amp; Ricotta Cheese.</div>
      <div class="item__row"><span>Veggie Calzone</span><span>$12.99</span></div>
      <div class="item__desc">Black Olives, Mushrooms, Onions, Green Peppers, Mozzarella,<br>&amp; Ricotta Cheese.</div>
      <div class="item__row"><span>Meat Lovers Calzone</span><span>$14.99</span></div>
      <div class="item__desc">Sausage, Pepperoni, Ham, Bacon, Mozzarella, &amp; Ricotta Cheese.</div>
    </div>
  </section>

  <aside class="toppings">
    <strong>Extra calzone toppings:</strong><br>
    <strong style="color:#2a1f00">$.75 each:</strong>
    <div class="opts">Anchovies | Banana Peppers | Black Olives | Green Olives<br>Extra Cheese | Extra Sauce | Garlic | Green Peppers | Ham |<br>Jalapeños | Meatballs | Mushrooms | Onions | Pepperoni |<br>Pineapple | Salami | Sausage | Spinach | Tomatoes | Bacon |<br>Broccoli.</div>
    <strong style="color:#2a1f00">$1.00 each:</strong>
    <div class="opts">Artichokes | Bacon | Chicken | Eggplant | Green Olives | Meatball |<br>Ricotta</div>
  </aside>

  <header class="hero">
    <svg width="270" height="14" viewBox="0 0 270 14" aria-hidden="true"><polygon points="0,0 270,0 135,14" fill="#2b2b2b"/></svg>
    <h1 class="brand"><div class="brand__top">Walt’s</div><div class="brand__bottom">Brick Oven Pizza</div></h1>
    <div class="brand__rule"></div>
    <p class="tagline tagline--a">· Stone Cooked Pizza<br>Wings · Cheesesteaks · Calzones</p>
    <svg class="star" width="30" height="30" viewBox="0 0 24 24" aria-hidden="true"><polygon fill="#c4161c" points="12,1 14.9,8.6 23,8.9 16.6,13.9 18.9,21.8 12,17.2 5.1,21.8 7.4,13.9 1,8.9 9.1,8.6"/></svg>
    <p class="fav fav__label">Owner's Favorite</p>
    <div class="fav__rule"></div>
    <p class="fav fav__name">Walt's Chicken &amp; Jalapeño<br>Built for Walt Himself.</p>
  </header>

  <section class="section" style="left:429px;top:453px;width:270px;height:87px">
    <h2 class="section__title">Drinks</h2>
    <div class="items">
      <div class="item__row" style="margin-top:2px"><span>20 oz Soda</span><span>$1.99</span></div>
      <div class="item__desc">Dr Fizz, Cola, Sparkle, Orange Soda, Diet Cola.</div>
      <div class="item__row" style="margin-top:2px"><span>2 Liter Soda</span><span>$2.99</span></div>
      <div class="item__desc">Dr Fizz, Cola, Sparkle, Orange Soda, Diet Cola.</div>
    </div>
  </section>

  <section class="section" style="left:429px;top:550px;width:270px;height:85px">
    <h2 class="section__title">Desserts</h2>
    <div class="items" style="line-height:17px">
      <div class="item__row" style="line-height:17px;margin-top:2px"><span>Cheesecake.</span><span>$4.99</span></div>
      <div class="item__row" style="line-height:17px"><span>Tiramisu.</span><span>$5.50</span></div>
      <div class="item__row" style="line-height:17px"><span>Cannoli.</span><span>$4.99</span></div>
    </div>
  </section>

  <section class="section" style="left:742px;top:50px;width:363px;height:197px">
    <h2 class="section__title">Pizza Rolls</h2>
    <div class="items">
      <div class="item__row"><span>Cheese Pizza Roll.</span><span>$11.49</span></div>
      <div class="item__row"><span>Pepperoni Pizza Roll</span><span>$12.99</span></div>
      <div class="item__desc">Pepperoni &amp; Cheese.</div>
      <div class="item__row"><span>Meat Lovers Pizza Roll</span><span>$13.99</span></div>
      <div class="item__desc">Pepperoni, Sausage, Ham, Bacon, &amp; Cheese.</div>
      <div class="item__row"><span>Veggie Pizza Roll</span><span>$13.99</span></div>
      <div class="item__desc">Mushrooms, Green Peppers, Onions, Black Olives, &amp; Cheese.</div>
      <div class="item__row"><span>Supreme Pizza Roll</span><span>$13.99</span></div>
      <div class="item__desc">Pepperoni, Sausage, Mushroom, Green Peppers, Onions, &amp; Cheese.</div>
      <div class="item__row"><span>Buffalo Chicken Pizza Roll</span><span>$13.99</span></div>
      <div class="item__desc">Buffalo Chicken &amp; Cheese.</div>
      <div class="item__row"><span>Chicken, Bacon, Jalapeños &amp; Ranch Pizza Roll</span><span>$13.99</span></div>
      <div class="item__desc">It is what it says, Plus Cheese.</div>
    </div>
  </section>

  <section class="section salad" style="left:742px;top:256px;width:363px;height:237px">
    <h2 class="section__title">Salads</h2>
    <div class="items">
      <div class="item__row" style="margin-top:3px"><span>Garden Salad</span><span class="sizes"><span>S</span>$4.99<i></i><span>M</span>$5.99<i></i><span>L</span>$8.99</span></div>
      <div class="item__desc">Lettuce, Tomatoes, Cucumbers, Olives, Onions, &amp; Pepperoncini.</div>
      <div class="item__row"><span>Antipasto</span><span class="sizes"><span>S</span>$6.99<i></i><span>M</span>$8.99<i></i><span>L</span>$11.99</span></div>
      <div class="item__desc">Ham, Salami, Lettuce, Tomatoes, Cucumbers, Olives, Onions, &amp; Pepperoncini. Topped with Mozzarella Cheese.</div>
      <div class="item__row"><span>Bruiser Chicken Salad</span><span class="sizes"><span>S</span>$6.99<i></i><span>M</span>$8.99<i></i><span>L</span>$11.99</span></div>
      <div class="item__desc">Chicken, Parmesan Cheese, Lettuce, Tomatoes, Cucumbers, Olives, Onions, &amp; Pepperoncini.</div>
      <div class="item__row"><span>Caesar Salad</span><span class="sizes"><span>S</span>$5.49<i></i><span>M</span>$6.99<i></i><span>L</span>$9.99</span></div>
      <div class="item__desc">Romaine Lettuce, Parmesan Cheese, Croutons - Tossed in Caesar Dressing.</div>
      <div class="item__row"><span>Chicken Caesar Salad</span><span class="sizes"><span>S</span>$6.99<i></i><span>M</span>$8.99<i></i><span>L</span>$11.99</span></div>
      <div class="item__desc">Chicken, Romaine Lettuce, Parmesan Cheese, Croutons - Tossed in Caesar Dressing.</div>
    </div>
  </section>

  <p class="dressings"><strong>Dressings:</strong><br>Ranch, Italian, Caesar, Blue Cheese, Balsamic, &amp; Vinaigrette.</p>

  <div class="photo" role="img" aria-label="Photo of a pizza with salami, tomatoes, olives and basil on a wooden table with green pepper rings"></div>
</main>
</body>
</html>
```